Eastfield Commercial Card

I would like a modern, eye catching card based off my logo design.
Info to include:
Anders Voll (Card Name)
eastfieldcommercial.example (Website)
555 203 8841 (Office/fax)
555 287 3096 (Business Cell)
anders@eastfieldcommercial.example (Work email)

Target Market(s)

Commercial real estate brokers, property owners.

Colors
ec1f27
757575

Requirements
Must have
• Name and info above. Not be lame!:)

```html
<!DOCTYPE html>
<html lang="en">
<head>
<meta charset="utf-8">
<title>Eastfield Commercial – Business Card</title>
<link rel="stylesheet" href="https://fonts.googleapis.com/css2?family=Montserrat:wght@400;500;700;800&display=swap">
<style>
  :root {
    --brand-red: #b21e24;
    --brand-red-bright: #ec1f27;
    --brand-grey: #757575;
    --charcoal: #3a3b3d;
    --card-dark: #2b2c2e;
    --card-dark-deep: #1f2022;
    --paper: #ffffff;
    --ink: #2a2a2a;
    --stage: #1c1d1f;
  }
  * { box-sizing: border-box; margin: 0; padding: 0; }
  html, body {
    width: 1200px; height: 900px; overflow: hidden;
    background: var(--stage);
    font-family: "Montserrat", Arial, sans-serif;
  }
  .canvas {
    position: relative; width: 1200px; height: 900px;
    display: flex; align-items: center; justify-content: center; gap: 50px;
  }
  .card {
    position: relative; width: 520px; height: 298px;
    border-radius: 22px; overflow: hidden;
  }

  /* Front: contact side */
  .card-front { background: var(--paper); }
  .card-front .shapes { position: absolute; inset: 0; }
  .name-banner {
    position: absolute; left: 0; top: 28px;
    width: 300px; height: 44px;
    background: var(--brand-red);
    display: flex; align-items: center; padding-left: 78px;
  }
  .name-banner .person-name {
    color: var(--paper); font-weight: 700; font-size: 24px; letter-spacing: 0.2px;
  }
  .badge-circle {
    position: absolute; left: 276px; top: 16px;
    width: 68px; height: 68px; border-radius: 50%;
    background: var(--paper); border: 2px solid var(--brand-red);
  }
  .contact-list {
    position: absolute; left: 22px; top: 98px;
    list-style: none; display: flex; flex-direction: column; gap: 9px;
  }
  .contact-item {
    display: flex; align-items: center; gap: 10px;
    font-size: 13.5px; font-weight: 500; color: var(--ink);
  }
  .contact-item .icon {
    width: 20px; height: 20px; border-radius: 50%;
    background: var(--charcoal);
    display: flex; align-items: center; justify-content: center; flex: none;
  }
  .contact-item .icon.red { background: var(--brand-red); }
  .contact-item .note { font-size: 11px; color: var(--brand-grey); margin-left: 4px; }

  /* Back: brand side */
  .card-back {
    background: linear-gradient(135deg, var(--card-dark) 0%, var(--card-dark-deep) 100%);
    display: flex; flex-direction: column; align-items: center; justify-content: center; gap: 14px;
    padding: 0 56px;
  }
  .brand-row { display: flex; align-items: center; gap: 12px; }
  .brand-square {
    width: 22px; height: 22px; border: 3px solid var(--paper); flex: none;
  }
  .brand-name {
    color: var(--brand-red); font-weight: 800; font-size: 25px;
    text-transform: uppercase; letter-spacing: 0.3px; white-space: nowrap;
  }
  .tagline-row { display: flex; align-items: center; gap: 12px; }
  .tagline-row .rule { width: 40px; height: 2px; background: var(--paper); }
  .tagline {
    color: var(--paper); font-weight: 500; font-size: 12px;
    letter-spacing: 3.2px; text-transform: uppercase; white-space: nowrap;
  }
</style>
</head>
<body>
<main class="canvas">

  <section class="card card-front" aria-label="Business card, contact side">
    <svg class="shapes" viewBox="0 0 520 298" width="520" height="298" aria-hidden="true">
      <polygon points="300,0 520,0 520,150 400,178" fill="var(--brand-red)"/>
      <polygon points="330,298 410,196 520,166 520,298" fill="var(--charcoal)"/>
      <polygon points="398,262 452,222 490,262" fill="var(--paper)"/>
    </svg>

    <div class="name-banner"><span class="person-name">Anders Voll</span></div>
    <div class="badge-circle"></div>

    <ul class="contact-list">
      <li class="contact-item">
        <span class="icon red"><svg width="12" height="12" viewBox="0 0 24 24"><path fill="#fff" d="M6.6 10.8a15 15 0 0 0 6.6 6.6l2.2-2.2a1 1 0 0 1 1-.25 11.4 11.4 0 0 0 3.6.57 1 1 0 0 1 1 1V20a1 1 0 0 1-1 1A17 17 0 0 1 3 4a1 1 0 0 1 1-1h3.5a1 1 0 0 1 1 1c0 1.250.2 2.45.57 3.57a1 1 0 0 1-.25 1z"/></svg></span>
        555 203 8841<span class="note">(office/fax)</span>
      </li>
      <li class="contact-item">
        <span class="icon red"><svg width="12" height="12" viewBox="0 0 24 24"><rect x="6" y="2" width="12" height="20" rx="2" fill="none" stroke="#fff" stroke-width="2.4"/><circle cx="12" cy="18" r="1.3" fill="#fff"/></svg></span>
        555 287 3096
      </li>
      <li class="contact-item">
        <span class="icon red"><svg width="12" height="12" viewBox="0 0 24 24"><rect x="2" y="5" width="20" height="14" rx="2" fill="none" stroke="#fff" stroke-width="2.2"/><path d="M3 6l9 7 9-7" fill="none" stroke="#fff" stroke-width="2.2"/></svg></span>
        anders@eastfieldcommercial.example
      </li>
      <li class="contact-item">
        <span class="icon"><svg width="12" height="12" viewBox="0 0 24 24"><circle cx="12" cy="12" r="9.5" fill="none" stroke="#fff" stroke-width="2"/><path d="M2.5 12h19M12 2.5c3 3 3 16 0 19M12 2.5c-3 3-3 16 0 19" fill="none" stroke="#fff" stroke-width="1.8"/></svg></span>
        www.eastfieldcommercial.example
      </li>
    </ul>
  </section>

  <section class="card card-back" aria-label="Business card, brand side">
    <div class="brand-row">
      <span class="brand-square"></span>
      <span class="brand-name">Eastfield Commercial</span>
    </div>
    <div class="tagline-row">
      <span class="rule"></span>
      <span class="tagline">Construction &amp; Roofing</span>
      <span class="rule"></span>
    </div>
  </section>

</main>
</body>
</html>
```